Men's and Boys sports themed barbershop. I was wanting to see what a black card would look like. I think white is too plain, but I am just needing some ideas for a design or background.

Contact Information for Business Card

Ace Trims
4826 E. Harbor Pine Rd
Pine Cove, Ga 34512
(428) 555-0142
ace_trims@quellmail.com
Denise Marlow (on one side) Gregory Marlow (on opposite side)
Owner
(428) 555-0163 (Denise) (352) 555-0163

```html
<!DOCTYPE html>
<html lang="en">
<head>
<meta charset="utf-8">
<title>Ace Trims business card, back</title>
<link rel="stylesheet" href="https://fonts.googleapis.com/css2?family=Open+Sans:wght@400;700&display=swap">
<style>
  :root {
    --backdrop: #9a9288;
    --card: #231f20;
    --accent: #0398db;
    --on-accent: #ffffff;
  }
  html, body {
    margin: 0;
    width: 1200px;
    height: 941px;
    overflow: hidden;
    background: var(--backdrop);
  }
  .stage {
    width: 1200px;
    height: 941px;
    display: flex;
    align-items: center;
    justify-content: center;
  }
  .card {
    width: 480px;
    height: 830px;
    display: block;
  }
  .card text {
    font-family: "Open Sans", sans-serif;
  }
  .card-bg { fill: var(--card); }
  .band { fill: var(--accent); }
  .rule { fill: var(--accent); }
  .brand-name { fill: var(--accent); font-weight: 700; font-size: 50px; }
  .brand-dot { fill: var(--accent); }
  .person-name, .person-role { fill: var(--on-accent); font-size: 32px; }
  .contact-line { fill: var(--accent); font-size: 21px; }
</style>
</head>
<body>
<main class="stage">
  <svg class="card" viewBox="0 0 480 830" xmlns="http://www.w3.org/2000/svg" aria-label="Business card back for Ace Trims">
    <defs>
      <clipPath id="card-shape">
        <rect width="480" height="830" rx="34"/>
      </clipPath>
    </defs>
    <rect class="card-bg" width="480" height="830" rx="34"/>
    <g clip-path="url(#card-shape)">
      <g transform="rotate(-42 240 415)">
        <rect class="rule" x="-400" y="330" width="1300" height="6"/>
        <rect class="band" x="-400" y="348" width="1300" height="112"/>
        <rect class="rule" x="-400" y="472" width="1300" height="6"/>

        <g class="brand">
          <circle class="brand-dot" cx="112" cy="286" r="14"/>
          <text class="brand-name" x="138" y="303">Ace Trims</text>
        </g>

        <text class="person-name" x="240" y="398" text-anchor="middle">GREGORY MARLOW</text>
        <text class="person-role" x="240" y="440" text-anchor="middle">Owner</text>

        <g class="contact">
          <text class="contact-line" x="90" y="526">4826 E. Harbor Pine Rd Pine Cove,</text>
          <text class="contact-line" x="90" y="554">Ga 34512</text>
          <text class="contact-line" x="90" y="582">P: (428) 555-0142</text>
          <text class="contact-line" x="90" y="610">C: (428) 555-0163</text>
          <text class="contact-line" x="90" y="638">ace_trims@quellmail.com</text>
          <text class="contact-line" x="90" y="666">acetrimsbarber.com</text>
        </g>
      </g>
    </g>
  </svg>
</main>
</body>
</html>
```